" A consultoria tributária (também denominada consultoria fiscal) é um leque de atividades voltadas às questões que demandam análise específica dos temas que geram tributos ou obrigações fiscais, numa empresa. "

```html
<!DOCTYPE html>
<html lang="pt-BR">
<head>
<meta charset="utf-8">
<title>Papel timbrado – Vantrix Consultoria Tributária</title>
<link href="https://fonts.googleapis.com/css2?family=Open+Sans:wght@400;600;700&display=swap" rel="stylesheet">
<style>
  :root{
    --backdrop:#e9eaec;
    --paper:#ffffff;
    --ink:#4a4d52;
    --ink-soft:#8a8e94;
    --gold:#c9962f;
    --band:#dde2ea;
    --band-ink:#6b7380;
    --watermark:#f2f3f5;
  }
  *{box-sizing:border-box;margin:0;padding:0}
  html,body{width:1200px;height:1200px;overflow:hidden;background:var(--backdrop)}
  body{font-family:"Open Sans",Arial,sans-serif;color:var(--ink)}
  .letterhead{
    position:absolute;left:204px;top:40px;width:792px;height:1120px;
    background:var(--paper);box-shadow:0 6px 24px rgba(0,0,0,.12);overflow:hidden;
  }
  .watermark{
    position:absolute;left:236px;top:360px;width:420px;height:420px;border-radius:50%;
    background:var(--watermark);
  }
  .brand{position:absolute;right:70px;top:64px;display:flex;align-items:center;gap:12px}
  .brand-dot{width:30px;height:30px;border-radius:50%;background:var(--gold)}
  .brand-name{font-size:34px;font-weight:700;color:var(--gold);letter-spacing:1px;line-height:1}
  .brand-tag{position:absolute;right:70px;top:106px;font-size:10px;color:var(--ink-soft);letter-spacing:1.5px;text-transform:uppercase}
  .recipient{position:absolute;left:150px;top:150px;font-size:13px;line-height:19px;font-weight:600}
  .date{position:absolute;right:70px;top:250px;font-size:12px;color:var(--ink-soft)}
  .letter-body{position:absolute;left:150px;right:70px;top:300px;font-size:13px;line-height:22px;text-align:justify}
  .letter-body p{margin-bottom:14px}
  .signature{
    position:absolute;left:110px;top:720px;width:150px;height:70px;
    background:linear-gradient(135deg,#f1f1f3,#e3e4e7);border-radius:4px;
  }
  .contact-band{
    position:absolute;left:0;right:0;bottom:0;height:74px;background:var(--band);
    display:flex;align-items:center;gap:44px;padding-left:60px;
    font-size:14px;color:var(--band-ink);
  }
  .contact-item{display:flex;align-items:center;gap:8px}
  .contact-item svg{width:16px;height:16px;fill:none;stroke:var(--band-ink);stroke-width:1.8}
</style>
</head>
<body>
  <main class="letterhead">
    <div class="watermark" aria-hidden="true"></div>

    <header class="brand">
      <span class="brand-dot" aria-hidden="true"></span>
      <span class="brand-name">VANTRIX</span>
    </header>
    <div class="brand-tag">consultoria tributária</div>

    <address class="recipient">
      To:<br>
      Sr. Marcos Vieira<br>
      Diretor Financeiro<br>
      Rua das Palmeiras, 210<br>
      Maringá, Paraná
    </address>

    <div class="date">Maringá, 12 de maio de 2024</div>

    <section class="letter-body">
      <p>Prezado senhor, apresentamos nossa proposta de consultoria tributária para o próximo exercício fiscal da sua empresa.</p>
      <p>Nossa equipe fará a análise detalhada dos tributos e das obrigações acessórias, identificando riscos, créditos recuperáveis e oportunidades de economia legal dentro das normas vigentes.</p>
      <p>Ao final de cada etapa, entregaremos um relatório claro com recomendações práticas e um calendário de prazos para a sua equipe contábil.</p>
      <p>Permanecemos à disposição para esclarecer qualquer dúvida.</p>
      <p>Atenciosamente,</p>
    </section>

    <div class="signature" role="img" aria-label="Assinatura manuscrita do responsável"></div>

    <footer class="contact-band">
      <span class="contact-item">
        <svg viewBox="0 0 16 16" aria-hidden="true"><path d="M4 2h2.5l1 3-1.5 1a8 8 0 0 0 4 4l1-1.5 3 1V12a2 2 0 0 1-2 2A11 11 0 0 1 2 4a2 2 0 0 1 2-2z"/></svg>
        (44) 3555-0188
      </span>
      <span class="contact-item">
        <svg viewBox="0 0 16 16" aria-hidden="true"><rect x="2" y="4" width="12" height="9" rx="1"/><path d="M2 5l6 4 6-4"/></svg>
        contato@vantrix.com.br
      </span>
      <span class="contact-item">
        <svg viewBox="0 0 16 16" aria-hidden="true"><circle cx="8" cy="8" r="6"/><path d="M2 8h12M8 2c2 2 2 10 0 12M8 2c-2 2-2 10 0 12"/></svg>
        www.vantrix.com.br
      </span>
    </footer>
  </main>
</body>
</html>
```